Transportation Brokerage and Freight Forwarder

We need a Facebook company page to attract potential customers (Shippers) and potential Drivers (Truck Drivers) for our business. We provide nationwide shipping services for contract customers in all areas of the Supply Chain LTL (Less than Truck Load), TL (Truck Load) Sea Freight (Ocean Vessels), Air Freight (Air Cargo), Container Freight, Rail Freight (Trains). We are also a Transportation Consulting Company as well helping clients to create Shipping solutions to improve there shipping capacity or cut cost by suggesting different modes of transport based upon their needs.

We have over 50+ years experience in the industry to include Driving (myself and my partner still hold CDL licenses currently), Dispatching Management, Operations Management and former Transport Executives, we are also doing work in other countries with our strategic partners in the form of Freight forwarding services that we offer.

Target Market(s)

The Transport and Shipping community in the U.S., Truck, Train, Ship, Plane & Container

Font styles to use
Serif
Sans Serif

Colors

Designer to choose colors to be used in the design.

Requirements
Must have
• Targeted services we provide (use our website for ideas) www.vornet.com. We want to get the name out there, use stock photos from the Logistics industry
Nice to have
• Appealing attraction to the page itself, want to draw views
Should not have
• No overkill of information

```html
<!DOCTYPE html>
<html lang="en">
<head>
<meta charset="utf-8">
<title>Freight Services Cover</title>
<link href="https://fonts.googleapis.com/css2?family=Montserrat:wght@800&family=Open+Sans:wght@400;600&display=swap" rel="stylesheet">
<style>
  :root {
    --page-bg: #e6e6e6;
    --navy: #0d3c78;
    --navy-deep: #082a5a;
    --sky: #5bbde0;
    --white: #ffffff;
    --edge-dark: #0a2f63;
  }
  html, body {
    margin: 0;
    padding: 0;
    width: 1200px;
    height: 1200px;
    overflow: hidden;
    background: var(--page-bg);
  }
  .cover {
    position: absolute;
    left: 20px;
    top: 380px;
    width: 1160px;
    height: 441px;
    box-shadow: 0 2px 6px rgba(0,0,0,0.25);
  }
  .headline { font-family: 'Montserrat', sans-serif; font-weight: 800; font-size: 49px; letter-spacing: -0.5px; }
  .headline-top { fill: var(--white); }
  .headline-bottom { fill: var(--sky); }
  .service-label { font-family: 'Open Sans', sans-serif; font-weight: 600; font-size: 15.5px; fill: var(--white); }
  .info-lead { font-family: 'Open Sans', sans-serif; font-size: 14px; fill: var(--sky); }
  .info-url { fill: var(--white); }
</style>
</head>
<body>
<svg class="cover" viewBox="0 0 820 312" xmlns="http://www.w3.org/2000/svg">
  <defs>
    <linearGradient id="navyFade" x1="0" y1="0" x2="1" y2="1">
      <stop offset="0" stop-color="#0f4585"/>
      <stop offset="1" stop-color="#082a5a"/>
    </linearGradient>
    <linearGradient id="truckScene" x1="0" y1="0" x2="0" y2="1">
      <stop offset="0" stop-color="#b79d75"/>
      <stop offset="0.45" stop-color="#d9d6d2"/>
      <stop offset="1" stop-color="#4c4f55"/>
    </linearGradient>
    <linearGradient id="trainScene" x1="0" y1="0" x2="1" y2="1">
      <stop offset="0" stop-color="#c9464a"/>
      <stop offset="0.5" stop-color="#c9ced6"/>
      <stop offset="1" stop-color="#6b7480"/>
    </linearGradient>
    <linearGradient id="airScene" x1="0" y1="0" x2="1" y2="1">
      <stop offset="0" stop-color="#8fa6c2"/>
      <stop offset="1" stop-color="#3d4b5e"/>
    </linearGradient>
    <linearGradient id="seaScene" x1="0" y1="0" x2="0" y2="1">
      <stop offset="0" stop-color="#7e9a77"/>
      <stop offset="0.5" stop-color="#eef1f4"/>
      <stop offset="1" stop-color="#5a6f86"/>
    </linearGradient>
  </defs>

  <rect class="cover-base" width="820" height="312" fill="url(#navyFade)"/>
  <rect class="container-yard" role="img" aria-label="Faint photo of stacked shipping containers" x="0" y="80" width="360" height="232" fill="#0e4078" opacity="0.5"/>

  <polygon class="accent-top" points="355,0 475,0 412,63" fill="var(--sky)"/>
  <polygon class="accent-bottom" points="355,312 480,312 410,242" fill="var(--sky)"/>

  <polygon class="photo-truck" role="img" aria-label="Photo of a red semi truck hauling a white trailer on a desert highway" points="656,0 820,0 820,312 656,312 500,156" fill="url(#truckScene)"/>
  <polygon class="photo-train" role="img" aria-label="Photo of a freight train with container cars" points="475,0 656,0 497,156 412,63" fill="url(#trainScene)"/>
  <polygon class="photo-air" role="img" aria-label="Photo of a cargo airplane at the airport" points="412,63 497,156 408,244 319,153" fill="url(#airScene)"/>
  <polygon class="photo-sea" role="img" aria-label="Photo of a container ship at sea" points="497,156 653,312 480,312 410,242" fill="url(#seaScene)"/>

  <g class="panel-edges" fill="none" stroke-linecap="square">
    <path d="M668,0 L512,156 L668,312" stroke="var(--edge-dark)" stroke-width="6"/>
    <path d="M660,0 L504,156 L660,312" stroke="var(--white)" stroke-width="3"/>
    <path d="M412,63 L497,156 L408,244 L319,153 Z" stroke="var(--white)" stroke-width="3"/>
    <path d="M475,0 L412,63" stroke="var(--white)" stroke-width="3"/>
    <path d="M410,242 L480,312" stroke="var(--white)" stroke-width="3"/>
    <circle cx="500" cy="155" r="6" fill="var(--edge-dark)" stroke="var(--white)" stroke-width="2"/>
  </g>

  <g class="chevrons" fill="var(--sky)">
    <polygon points="310,125 283,155 310,185 322,185 295,155 322,125"/>
    <polygon points="328,125 301,155 328,185 336,185 309,155 336,125" opacity="0.7"/>
  </g>

  <g class="service-tags">
    <rect x="436" y="57" width="108" height="32" fill="var(--sky)"/>
    <text class="service-label" x="444" y="79">Train Freight</text>
    <rect x="349" y="170" width="96" height="33" fill="var(--sky)"/>
    <text class="service-label" x="357" y="192">Air Freight</text>
    <rect x="629" y="245" width="118" height="35" fill="var(--sky)"/>
    <text class="service-label" x="638" y="268">Truck Freight</text>
    <rect x="464" y="272" width="97" height="34" fill="var(--sky)"/>
    <text class="service-label" x="472" y="294">Sea Freight</text>
  </g>

  <text class="headline headline-top" x="21" y="71">WE LISTEN</text>
  <text class="headline headline-bottom" x="21" y="117">WE DELIVER</text>
  <line class="headline-rule" x1="22" y1="124" x2="290" y2="124" stroke="var(--sky)" stroke-width="0.8" opacity="0.6"/>

  <text class="info-lead" x="39" y="281">For More info: <tspan class="info-url">www.vornet.com</tspan></text>
</svg>
</body>
</html>
```